Criação de Logotipo + Papelaria Profissional + Manual para Contabilidade & Finanças
" Possui planos de investimentos e o cliente realiza a contratação e recebe rendimentos diários "

```html
<!DOCTYPE html>
<html lang="pt-BR">
<head>
<meta charset="utf-8">
<title>Navero Investimentos – Papelaria</title>
<link rel="stylesheet" href="https://fonts.googleapis.com/css2?family=Comfortaa:wght@400;700&display=swap">
<style>
  :root {
    --backdrop: #f1f2f3;
    --paper: #ffffff;
    --navy: #1c4d78;
    --navy-deep: #173f63;
    --green: #3ba47b;
    --flap-top: #6d74b4;
    --flap-bottom: #2db37c;
    --ghost: rgba(255,255,255,0.07);
    --ink-light: #dfe9f2;
  }
  * { box-sizing: border-box; margin: 0; padding: 0; }
  html, body { width: 1200px; height: 1200px; overflow: hidden; }
  body {
    background: var(--backdrop);
    font-family: "Comfortaa", sans-serif;
    position: relative;
  }
  .letterhead {
    position: absolute;
    left: 70px; top: 230px;
    width: 520px; height: 740px;
    background: var(--paper);
    box-shadow: 0 0 0 1px #e3e5e8;
  }
  .letterhead__brand {
    position: absolute;
    top: 52px; left: 0; right: 0;
    text-align: center;
    color: var(--green);
    font-weight: 700;
    font-size: 54px;
    letter-spacing: 1px;
  }
  .letterhead__band {
    position: absolute;
    left: 0; right: 0; bottom: 0;
    height: 22px;
    background: var(--navy);
  }
  .envelope {
    position: absolute;
    left: 620px; top: 100px;
    width: 510px; height: 740px;
    background: var(--navy);
    overflow: hidden;
  }
  .envelope__flap {
    position: absolute;
    top: 0; left: 0; right: 0;
    height: 120px;
    background: linear-gradient(to bottom, var(--flap-top), var(--flap-bottom));
  }
  .envelope__ghost-name {
    position: absolute;
    top: 220px; left: 0; right: 0;
    text-align: center;
    color: var(--ghost);
    font-weight: 700;
    font-size: 150px;
  }
  .envelope__brand {
    position: absolute;
    right: 36px; top: 525px;
    color: var(--green);
    font-weight: 700;
    font-size: 54px;
  }
  .envelope__rule {
    position: absolute;
    left: 28px; right: 28px; top: 618px;
    height: 2px;
    background: var(--ink-light);
  }
  .envelope__contact {
    position: absolute;
    left: 28px; top: 630px;
    color: var(--ink-light);
    font-size: 10.5px;
    line-height: 1.6;
  }
  .envelope__contact strong { font-weight: 700; }
  .envelope__web {
    position: absolute;
    right: 28px; top: 630px;
    text-align: right;
    color: var(--ink-light);
    font-size: 9px;
  }
  .envelope__social {
    display: flex; gap: 6px;
    justify-content: flex-end;
    margin-top: 10px;
  }
  .envelope__social span {
    width: 13px; height: 13px;
    border-radius: 50%;
    background: var(--ink-light);
  }
</style>
</head>
<body>
  <section class="letterhead" aria-label="Papel timbrado">
    <div class="letterhead__brand">navero</div>
    <div class="letterhead__band"></div>
  </section>

  <section class="envelope" aria-label="Envelope">
    <div class="envelope__flap"></div>
    <div class="envelope__ghost-name" aria-hidden="true">navero</div>
    <div class="envelope__brand">navero</div>
    <div class="envelope__rule"></div>
    <address class="envelope__contact">
      <strong>Navero Investimentos</strong><br>
      Rua das Palmeiras, 480 cj. 12<br>
      01310-200 - Campinas - SP<br>
      Tel.: 11 4000-2121
    </address>
    <div class="envelope__web">
      www.naveroinvest.com.br
      <div class="envelope__social" aria-label="Redes sociais">
        <span></span><span></span><span></span><span></span><span></span>
      </div>
    </div>
  </section>
</body>
</html>
```